Bold Flyer Needed for Bold Little Gym

We need a 1 page flyer created for our small boutique fitness facility, KorVesta, which highlights a new service we are offering.
We are now offering Red Light Therapy (RLT) to our members and I need a full color, 1 page flyer created that captures the eye of our members while highlighting the benefits and clearly stating the prices at the bottom of the page.
Flyer will be printed out on a standard 8.5" x 11" sheet of paper and should be laid out in a way that is easy to read. Landscape or Portrait layouts are both expectable.
We are using Quorvane Glow Therapy Lights TelaRix 700 Lamps as found here http://lnkzo.example/7QWPL4M
I have attached the text that should be included and our logo for branding of the flyer.
Thank you!

```html
<!DOCTYPE html>
<html lang="en">
<head>
<meta charset="utf-8">
<title>KorVesta Red Light Therapy Flyer</title>
<link href="https://fonts.googleapis.com/css2?family=Anton&family=Lato:wght@400;700;900&display=swap" rel="stylesheet">
<style>
  :root{
    --yellow:#f7cf00;
    --yellow-soft:#f9e27a;
    --black:#0d0d0d;
    --charcoal:#3a3a3a;
    --red:#e8141c;
    --blue:#1a8ef0;
    --ink:#161616;
    --paper:#ffffff;
    --stage:#cbcbcb;
  }
  *{box-sizing:border-box;margin:0;padding:0}
  html,body{width:1200px;height:1024px;overflow:hidden;background:var(--stage)}
  .flyer{position:absolute;left:0;top:88px;width:1200px;height:848px;background:var(--paper);overflow:hidden;font-family:'Lato',sans-serif;color:var(--ink)}
  .display{font-family:'Anton',sans-serif;font-weight:400;text-transform:uppercase;letter-spacing:.2px}
  .hero-band{position:absolute;left:0;top:0;width:100%;height:200px}
  .headline{position:absolute;left:40px;top:38px;font-size:29px;line-height:37px;color:var(--black)}
  .headline .hot{color:var(--red)}
  .brand{position:absolute;left:902px;top:42px;width:262px;text-align:center}
  .brand-name{font-family:'Anton',sans-serif;font-size:60px;line-height:70px;color:#fff}
  .brand-tag{font-family:'Lato',sans-serif;font-weight:900;font-size:9px;letter-spacing:2.4px;color:var(--yellow);margin-top:2px}
  .athlete-photo{position:absolute;left:0;top:192px;width:245px;height:656px;
    background:linear-gradient(160deg,#7a2a4e 0%,#5a2a6e 35%,#8d1b25 60%,#1b0d18 100%);
    clip-path:polygon(0 0,62% 0,70% 6%,80% 10%,82% 22%,88% 30%,96% 40%,92% 55%,85% 70%,78% 85%,70% 100%,0 100%)}
  .section-tab{position:absolute;height:44px;color:var(--yellow);font-size:22px;line-height:44px;padding-left:20px}
  .section-tab svg{position:absolute;left:0;top:0}
  .section-tab span{position:relative}
  .copy{position:absolute;font-size:14px;line-height:18.5px}
  .copy b{font-weight:700}
  .copy .hot{color:var(--red);font-weight:700}
  .why-list{position:absolute;left:251px;top:544px;width:270px;list-style:none;font-size:14px;line-height:18.5px}
  .why-list li{margin-bottom:12px}
  .why-list .label{font-weight:700;display:block;text-transform:uppercase}
  .benefit{position:absolute;width:230px;font-size:14px;line-height:18.5px;padding-left:27px}
  .benefit b{display:block;font-weight:700}
  .benefit svg{position:absolute;left:0;top:0}
  .benefit::after{content:"";position:absolute;left:9px;top:22px;width:1.5px;height:40px;background:var(--ink)}
  .benefit.last::after{height:18px}
  .device-photo{position:absolute;left:1037px;top:149px;width:110px;height:370px;border-radius:6px;
    background:radial-gradient(circle at 50% 50%,#ff6a6a 0%,#e23a3a 55%,#c8c8c8 100%)}
  .offer{position:absolute;left:538px;top:519px;width:323px;height:254px;text-align:center}
  .offer-text{position:absolute;left:0;top:20px;width:100%}
  .offer .kicker{color:var(--red);font-size:19px}
  .offer .lead{font-size:20px;line-height:22px;margin-top:6px;color:var(--black)}
  .offer .reg{font-size:10px;margin-top:2px}
  .offer .limited{color:var(--red);font-size:19px;margin-top:8px}
  .offer .cta{font-family:'Anton',sans-serif;font-size:12.5px;line-height:15px;margin-top:2px}
  .facility{position:absolute;left:880px;top:550px;width:296px;text-align:center;color:var(--blue);font-size:20.5px;line-height:24px}
  .prices{position:absolute;left:885px;top:605px;width:286px;border-collapse:collapse;border:2.5px solid var(--black);font-family:'Anton',sans-serif;font-size:12.5px}
  .prices th{background:var(--black);color:var(--yellow);height:41px;font-weight:400;line-height:13px;border-left:2px solid #555}
  .prices th:first-child{text-align:left;padding-left:12px;border-left:0}
  .prices td{height:26px;text-align:center;border-left:2px solid var(--black);color:var(--black)}
  .prices td:first-child{text-align:left;padding-left:12px;border-left:0}
  .prices tr:nth-child(odd) td{background:var(--yellow)}
  .prices tr:nth-child(even) td{background:var(--yellow-soft)}
  .footer-band{position:absolute;left:0;top:790px;width:100%;height:58px}
  .ready{position:absolute;left:176px;top:802px;color:var(--yellow);font-size:25px}
  .visit{position:absolute;left:449px;top:805px;font-size:23px;color:var(--black);letter-spacing:.1px}
</style>
</head>
<body>
<main class="flyer">
  <svg class="hero-band" viewBox="0 0 1200 200" aria-hidden="true">
    <polygon points="0,0 767,0 873,177 0,177" fill="var(--yellow)"/>
    <polygon points="767,0 1200,0 1200,196 906,196" fill="var(--black)"/>
    <polygon points="1094,0 1200,0 1200,196 1050,196" fill="var(--charcoal)"/>
    <rect x="90" y="182" width="430" height="4" fill="var(--black)"/>
  </svg>

  <h1 class="headline display">
    Unlock your potential with <span class="hot">red light therapy</span> at KorVesta!<br>
    Introducing our new <span class="hot">red light therapy</span> room!<br>
    Transform your wellness routine with the power of light!
  </h1>

  <div class="brand">
    <div class="brand-name">KorVesta</div>
    <div class="brand-tag">PERSONAL GROUP TRAINING</div>
  </div>

  <div class="athlete-photo" role="img" aria-label="Athlete lifting a dumbbell in red and purple studio light"></div>

  <h2 class="section-tab display" style="left:235px;top:230px;width:295px">
    <svg width="295" height="44" viewBox="0 0 295 44" aria-hidden="true"><polygon points="0,0 272,0 295,44 0,44" fill="var(--black)"/><polygon points="275,0 295,0 295,34" fill="var(--yellow)"/></svg>
    <span>What is red light therapy?</span>
  </h2>
  <p class="copy" style="left:251px;top:292px;width:275px">
    <b>Red Light Therapy (RLT)</b> is a revolutionary treatment that uses specific wavelengths of light to promote healing, reduce inflam­mation, and enhance overall well-being. At KorVesta, we are excited to offer the advanced <span class="hot">Quorvane Glow Therapy TelaRix 700 panels</span>—designed to maximize your health benefits in a relaxing environment.
  </p>

  <h2 class="section-tab display" style="left:235px;top:474px;width:295px">
    <svg width="295" height="44" viewBox="0 0 295 44" aria-hidden="true"><polygon points="0,0 272,0 295,44 0,44" fill="var(--black)"/><polygon points="275,0 295,0 295,34" fill="var(--yellow)"/></svg>
    <span>Why choose KorVesta?</span>
  </h2>
  <ul class="why-list">
    <li><span class="label">State-of-the-art equipment:</span>Experience the power of eight Quorvane Glow Therapy TelaRix 700 panels—some of the best on the market!</li>
    <li><span class="label">Expert guidance:</span>Our trained staff will guide you through each session to ensure you get the most out of your therapy.</li>
    <li><span class="label">Community focused:</span>Join a supportive community that prioritizes health &amp; wellness.</li>
  </ul>

  <h2 class="section-tab display" style="left:558px;top:230px;width:418px">
    <svg width="418" height="44" viewBox="0 0 418 44" aria-hidden="true"><polygon points="0,0 395,0 418,44 0,44" fill="var(--black)"/><polygon points="398,0 418,0 418,34" fill="var(--yellow)"/></svg>
    <span>Benefits of red light therapy:</span>
  </h2>

  <div class="benefit" style="left:558px;top:295px"><svg width="19" height="19" viewBox="0 0 20 20" aria-hidden="true"><circle cx="10" cy="10" r="10" fill="var(--yellow)"/><path d="M5.5 10.5l3 3 6-6.5" stroke="#fff" stroke-width="2.4" fill="none"/></svg><b>Boosts Energy Levels:</b>Feel revitalized &amp; more energetic after each session.</div>
  <div class="benefit" style="left:558px;top:369px"><svg width="19" height="19" viewBox="0 0 20 20" aria-hidden="true"><circle cx="10" cy="10" r="10" fill="var(--yellow)"/><path d="M5.5 10.5l3 3 6-6.5" stroke="#fff" stroke-width="2.4" fill="none"/></svg><b>Enhances Muscle Recovery:</b>Speed up recovery times post-workout &amp; reduce soreness.</div>
  <div class="benefit last" style="left:558px;top:443px"><svg width="19" height="19" viewBox="0 0 20 20" aria-hidden="true"><circle cx="10" cy="10" r="10" fill="var(--yellow)"/><path d="M5.5 10.5l3 3 6-6.5" stroke="#fff" stroke-width="2.4" fill="none"/></svg><b>Improves Skin Health:</b>Reduce wrinkles, blemishes, &amp; promote a youthful glow.</div>
  <div class="benefit" style="left:803px;top:295px"><svg width="19" height="19" viewBox="0 0 20 20" aria-hidden="true"><circle cx="10" cy="10" r="10" fill="var(--yellow)"/><path d="M5.5 10.5l3 3 6-6.5" stroke="#fff" stroke-width="2.4" fill="none"/></svg><b>Supports Joint Health:</b>Alleviate pain &amp; inflammation, making movement easier.</div>
  <div class="benefit" style="left:803px;top:369px"><svg width="19" height="19" viewBox="0 0 20 20" aria-hidden="true"><circle cx="10" cy="10" r="10" fill="var(--yellow)"/><path d="M5.5 10.5l3 3 6-6.5" stroke="#fff" stroke-width="2.4" fill="none"/></svg><b>Promotes Better Sleep:</b>Improve your sleep patterns and overall restfulness.</div>
  <div class="benefit last" style="left:803px;top:443px"><svg width="19" height="19" viewBox="0 0 20 20" aria-hidden="true"><circle cx="10" cy="10" r="10" fill="var(--yellow)"/><path d="M5.5 10.5l3 3 6-6.5" stroke="#fff" stroke-width="2.4" fill="none"/></svg><b>Increases Circulation:</b>Enhance blood flow for better nutrient delivery to muscles.</div>

  <div class="device-photo" role="img" aria-label="Red light therapy LED panel standing upright"></div>

  <section class="offer">
    <svg width="323" height="254" viewBox="0 0 323 254" aria-hidden="true" style="position:absolute;left:0;top:0">
      <polygon points="40,18 300,0 290,40 323,60 305,120 320,190 300,230 60,254 20,220 0,150 15,90 5,40" fill="var(--yellow)"/>
    </svg>
    <div class="offer-text">
      <div class="kicker display">Special introductory offer!</div>
      <div class="lead display">Try your first<br>session for just $25!</div>
      <div class="reg display">(Regularly $55)</div>
      <div class="limited display">Limited time only</div>
      <div class="cta">Book your session today and<br>discover how Red Light Therapy can<br>elevate your fitness</div>
    </div>
  </section>

  <p class="facility display">KorVesta fitness facility,<br>your wellness, our commitment!</p>

  <table class="prices">
    <thead><tr><th>PRICES:</th><th>KORVESTA<br>MEMBER</th><th>NON-<br>MEMBER</th></tr></thead>
    <tbody>
      <tr><td>Single Session</td><td>$35</td><td>$55</td></tr>
      <tr><td>3-Pack</td><td>$102</td><td>$159</td></tr>
      <tr><td>5-Pack</td><td>$167</td><td>$259</td></tr>
      <tr><td>10-Pack</td><td>$316</td><td>$491</td></tr>
    </tbody>
  </table>

  <svg class="footer-band" viewBox="0 0 1200 58" aria-hidden="true">
    <polygon points="380,12 1200,0 1200,58 416,58" fill="var(--yellow)"/>
    <polygon points="170,4 362,4 403,58 170,58" fill="var(--charcoal)"/>
    <polygon points="0,4 170,4 170,58 0,58" fill="var(--black)" opacity=".0"/>
  </svg>
  <div class="ready display">Ready to shine?</div>
  <div class="visit display" style="text-transform:none">Visit our front desk or call us at (555) 214- 0386 to schedule your appointment.</div>
</main>
</body>
</html>
```